Broschüren-Design für Bettenmanufaktur
Super Design, super schnelle Reaktion, super netter Kontakt!
Zielgruppe
Wir sind eine Bettenmanufaktur die Futonbetten und Himmelbetten aus Metall herstellt, geziert mit Leder- oder Holzelementen an den Bettseiten und Rückenlehnen. Das besondere ist, dass es Systembetten sind. Man kann später aus seinen Futonbett noch ein Himmelbett machen, oder die Leder- und Holzelemente einfach tauschen. Unsere Zielgruppe sind Paare die auf Design und Still stehen, sowie auf Paare die Lust auf Mehr als nur ein Bett haben.
Aufgabenstellung
Bitte an unsere neue Homepage vom Design/Still anpassen: www.pelvoran-design.de
Die Broschüre soll als Zulage bei anderen Bestellungen beiliegen und auf Messen verteilt werden.

```html
<!DOCTYPE html>
<html lang="de">
<head>
<meta charset="utf-8">
<title>Pelvoran Broschüre</title>
<link href="https://fonts.googleapis.com/css2?family=Josefin+Sans:ital,wght@0,300;0,400;0,600;1,400&family=Rajdhani:wght@600;700&display=swap" rel="stylesheet">
<style>
  :root {
    --red: #b8342a;
    --red-box: #c23a2f;
    --photo-dark: #2a2624;
    --photo-mid: #4a413b;
    --photo-warm: #6d5a4c;
    --ink-dark: #2b211f;
    --white: #ffffff;
    --accent: #e0452f;
    --stage: #f4f4f4;
  }
  * { box-sizing: border-box; margin: 0; padding: 0; }
  html, body { width: 1200px; height: 800px; overflow: hidden; background: var(--stage); }
  .spread {
    position: absolute; left: 100px; top: 46px;
    width: 1000px; height: 708px; display: flex;
    box-shadow: 0 10px 30px rgba(0,0,0,.15);
  }
  .panel { position: relative; width: 500px; height: 708px; overflow: hidden; }

  /* inner panel */
  .inner { background: var(--red); color: var(--white); font-family: "Josefin Sans", sans-serif; }
  .inner-photo {
    position: absolute; right: 0; top: 0; width: 150px; height: 100%;
    background: linear-gradient(180deg, var(--photo-warm), var(--photo-mid) 55%, var(--photo-dark));
  }
  .inner-content { position: absolute; left: 0; top: 0; width: 350px; height: 100%; padding: 30px 30px 0 34px; }
  .quote-mark { font-family: Georgia, serif; font-weight: 700; font-size: 96px; line-height: .8; height: 48px; }
  .claim { margin-top: 18px; font-size: 25px; font-weight: 400; line-height: 1.42; letter-spacing: 1.5px; }
  .feather {
    position: absolute; left: 188px; top: 34px; width: 150px; height: 120px;
    background: radial-gradient(ellipse at center, rgba(255,255,255,.3), rgba(255,255,255,0) 70%);
  }
  .intro { margin-top: 26px; font-size: 14px; font-weight: 400; line-height: 1.55; letter-spacing: .6px; }
  .intro p + p { margin-top: 16px; }
  .contact-title { margin-top: 36px; font-family: "Rajdhani", sans-serif; font-weight: 700; font-size: 32px; letter-spacing: 1px; }
  .contact { margin-top: 8px; font-size: 13px; line-height: 1.5; letter-spacing: .4px; font-style: normal; }
  .contact .lines { margin-top: 14px; }

  /* cover panel */
  .cover {
    background: linear-gradient(170deg, var(--photo-warm) 0%, var(--photo-mid) 40%, var(--photo-dark) 100%);
    color: var(--white);
  }
  .brand-top { position: absolute; left: 24px; top: 22px; font-family: "Josefin Sans", sans-serif; font-weight: 600; font-size: 26px; display: flex; align-items: center; gap: 8px; }
  .brand-top .dot { width: 10px; height: 10px; border-radius: 50%; background: var(--white); }
  .cover-quote { position: absolute; right: 22px; top: 56px; font-family: Georgia, serif; font-weight: 700; font-size: 56px; line-height: .8; }
  .bed-types { position: absolute; right: 22px; top: 100px; text-align: right; font-family: "Josefin Sans", sans-serif; font-style: italic; font-size: 24px; line-height: 1.45; letter-spacing: 1.5px; }
  .headline-box {
    position: absolute; right: 0; top: 262px; width: 320px;
    background: var(--red-box); border: 2px solid rgba(255,255,255,.35); border-right: none;
    font-family: "Rajdhani", sans-serif; font-weight: 700; text-align: center;
    padding: 22px 10px 24px;
  }
  .headline-box .wishes { color: var(--ink-dark); font-weight: 700; font-size: 29px; line-height: 1.12; letter-spacing: .5px; }
  .headline-box .system { margin-top: 18px; color: var(--white); font-weight: 700; font-size: 29px; line-height: 1.12; letter-spacing: .5px; }
  .brand-bottom { position: absolute; right: 22px; bottom: 66px; font-family: "Josefin Sans", sans-serif; font-weight: 600; font-size: 24px; letter-spacing: 2px; color: var(--accent); }
</style>
</head>
<body>
<main class="spread">
  <section class="panel inner">
    <div class="inner-photo" role="img" aria-label="Foto: Himmelbett aus Metall mit Vorhängen und roter Bettwäsche"></div>
    <div class="inner-content">
      <div class="quote-mark">“</div>
      <div class="feather" role="img" aria-label="Illustration: weiße Feder"></div>
      <h2 class="claim">Sinnlich.<br>Exklusiv.<br>Fesselnd.</h2>
      <div class="intro">
        <p>Tauchen Sie ein in eine Atmosphäre vollkommener Entspannung und erleben Sie einzigartigen Komfort.</p>
        <p>Was auch immer Sie in Ihrem Bett erleben möchten, der Rahmen bewegt sich nicht.</p>
        <p>Dank dem Baukastenprinzip, passt sich Ihr Pelvoran-Metallbett an, sobald Sie sich Veränderung wünschen oder neue erotische Horizonte erkunden möchten.</p>
      </div>
      <h3 class="contact-title">KONTAKT</h3>
      <address class="contact">
        Pelvoran GmbH<br>Lindenallee 12<br>52062 Talbrunn
        <div class="lines">Telefon: 0151/20394817 (nur Anrufe)<br>E-Mail: service@pelvoran-design.de<br>Website: https://pelvoran-design.de</div>
      </address>
    </div>
  </section>

  <section class="panel cover" role="img" aria-label="Foto: Metall-Himmelbett mit weißen Vorhängen und roten Kissen im gedämpften Licht">
    <div class="brand-top">wolkenfalter <span class="dot"></span></div>
    <div class="cover-quote">“</div>
    <p class="bed-types">Futonbett.<br>Himmelbett.<br>Lustbett.</p>
    <div class="headline-box">
      <p class="wishes">IHRE WÜNSCHE.<br>IHRE NÄCHTE.<br>IHRE TRÄUME.</p>
      <p class="system">UNSER METALL-<br>SYSTEMBETT.</p>
    </div>
    <div class="brand-bottom">PELVORAN</div>
  </section>
</main>
</body>
</html>
```